Business Card Design

I have a very clear idea of what I want. I just do not know how to do the graphic design to match it.

On the front I want the uploaded image with the horse and the two people.
I want

Bottom left hand corner
Lewis Brand
0438 512 607

Bottom right
There is maroon block with Neil Patton Practitioner Group Logo
Next to that I want the Stable Arc tile about the same size ( attached psd file)

On the back I want a plain colour (white) with the information

Lewis Brand
Equine Performance
Rowland4Ponies and Acupuncture
Horsemanship Lessons and Clinics
Horse Training

lbrand@fauna812.com.au
FB/lewis.brand.207
StableArc.com.au

Industry/Entity Type

Business

Contact Information for Business Card

Lewis Brand
0438 512 607
lbrand@fauna812.com.au

```html
<!DOCTYPE html>
<html lang="en">
<head>
<meta charset="utf-8">
<title>Lewis Brand – Business Card</title>
<link rel="stylesheet" href="https://fonts.googleapis.com/css2?family=Arimo:wght@400;700&family=Roboto+Condensed:wght@400&family=Playfair+Display+SC:wght@400&family=Great+Vibes&display=swap">
<style>
  :root {
    --bg: #e9e6e1;
    --card-white: #ffffff;
    --navy: #1f3f73;
    --navy-soft: #2c4f86;
    --brown: #5a3418;
    --brown-dark: #3f230f;
    --cream: #f3e6cf;
    --maroon: #6b2414;
    --sand-light: #d8c29a;
    --sand-mid: #b99a68;
    --sand-dark: #8e6f45;
    --ink: #3a2412;
  }
  * { box-sizing: border-box; margin: 0; padding: 0; }
  html, body { width: 1200px; height: 843px; overflow: hidden; background: var(--bg); }
  .canvas {
    position: relative; width: 1200px; height: 843px;
    display: flex; align-items: center; justify-content: center; gap: 40px;
  }
  .card {
    position: relative; width: 560px; height: 342px; overflow: hidden;
    box-shadow: 0 4px 14px rgba(0,0,0,0.18);
  }

  /* ---------- Back ---------- */
  .card-back { background: var(--card-white); }
  .brand-tile {
    position: absolute; left: 44px; top: 60px; width: 104px; height: 104px;
    border-radius: 18px; background: var(--brown);
    padding: 8px;
  }
  .brand-tile-inner {
    width: 100%; height: 100%; border-radius: 12px; background: var(--card-white);
    display: flex; align-items: center; justify-content: center;
    font-family: "Arimo", sans-serif; font-weight: 700; font-size: 15px; color: var(--navy);
  }
  .back-name {
    position: absolute; left: 44px; top: 190px;
    font-family: "Arimo", sans-serif; font-weight: 700; font-size: 26px; color: var(--navy);
  }
  .services {
    position: absolute; left: 44px; top: 226px; list-style: none;
    font-family: "Arimo", sans-serif; font-weight: 700; font-size: 13.5px; line-height: 18px; color: var(--navy-soft);
  }
  .contacts {
    position: absolute; right: 28px; top: 196px; list-style: none;
    font-family: "Arimo", sans-serif; font-size: 13px; line-height: 22px; color: var(--navy);
    text-align: right;
  }
  .contacts li { display: flex; align-items: center; justify-content: flex-end; gap: 8px; }
  .contacts svg { width: 13px; height: 13px; flex: none; }

  /* ---------- Front ---------- */
  .card-front { background: var(--sand-mid); }
  .front-photo {
    position: absolute; left: 72px; top: 0; right: 0; bottom: 0;
    background: radial-gradient(ellipse at 50% 30%, var(--sand-light) 0%, var(--sand-mid) 60%, var(--sand-dark) 100%);
  }
  .front-band {
    position: absolute; left: 0; top: 0; width: 72px; height: 100%;
    background: linear-gradient(90deg, var(--brown-dark), var(--brown));
    display: flex; align-items: center; justify-content: center;
  }
  .band-text {
    writing-mode: vertical-rl; transform: rotate(180deg);
    font-family: "Roboto Condensed", sans-serif; color: var(--cream);
    font-size: 27px; line-height: 30px; letter-spacing: 0.5px;
  }
  .headline {
    position: absolute; left: 120px; right: 40px; top: 22px; text-align: center; color: var(--ink);
  }
  .headline-kicker {
    font-family: "Playfair Display SC", serif; font-size: 17px; letter-spacing: 1.5px;
  }
  .headline-script {
    font-family: "Great Vibes", cursive; font-size: 62px; line-height: 62px; margin-top: 2px;
  }
  .headline-swoosh { position: absolute; left: 40px; top: 92px; width: 320px; height: 30px; }
  .front-tile {
    position: absolute; right: 106px; bottom: 30px; width: 56px; height: 56px;
    border-radius: 11px; background: var(--brown); padding: 5px;
  }
  .front-tile .brand-tile-inner { border-radius: 7px; font-size: 9px; }
  .partner-block {
    position: absolute; right: 28px; bottom: 26px; width: 68px; height: 64px;
    background: var(--maroon); color: var(--cream);
    display: flex; align-items: center; justify-content: center; text-align: center;
    font-family: "Arimo", sans-serif; font-size: 8px; line-height: 10px; padding: 4px;
  }
</style>
</head>
<body>
<main class="canvas">

  <section class="card card-back" aria-label="Card back">
    <div class="brand-tile"><div class="brand-tile-inner">Stable Arc</div></div>
    <h1 class="back-name">Lewis Brand</h1>
    <ul class="services">
      <li>Equine Performance</li>
      <li>Rowland4Ponies &amp; Acupuncture</li>
      <li>Horsemanship Lessons &amp; Clinics</li>
      <li>Horse Training</li>
    </ul>
    <ul class="contacts">
      <li>lbrand@fauna812.com.au
        <svg viewBox="0 0 13 13" aria-hidden="true"><rect x="0.5" y="2.5" width="12" height="8" fill="none" stroke="#1f3f73"/><path d="M0.5 2.5 L6.5 7 L12.5 2.5" fill="none" stroke="#1f3f73"/></svg></li>
      <li>www.StableArc.com.au
        <svg viewBox="0 0 13 13" aria-hidden="true"><circle cx="6.5" cy="6.5" r="5.8" fill="none" stroke="#1f3f73"/><ellipse cx="6.5" cy="6.5" rx="2.6" ry="5.8" fill="none" stroke="#1f3f73"/><line x1="0.7" y1="6.5" x2="12.3" y2="6.5" stroke="#1f3f73"/></svg></li>
      <li>FB/lewis.brand.207
        <svg viewBox="0 0 13 13" aria-hidden="true"><rect x="0.5" y="0.5" width="12" height="12" fill="#1f3f73"/></svg></li>
    </ul>
  </section>

  <section class="card card-front" aria-label="Card front">
    <div class="front-photo" role="img" aria-label="Photo of a trainer and a handler working a bay horse on a sandy arena"></div>
    <div class="front-band">
      <p class="band-text">Lewis Brand<br>0438 512 607</p>
    </div>
    <div class="headline">
      <p class="headline-kicker">HOW YOU EVER GONNA KNOW</p>
      <p class="headline-script">Your Potential</p>
      <svg class="headline-swoosh" viewBox="0 0 320 30" aria-hidden="true"><path d="M5 22 Q160 2 315 20" fill="none" stroke="#3a2412" stroke-width="2"/></svg>
    </div>
    <div class="front-tile"><div class="brand-tile-inner">Stable Arc</div></div>
    <div class="partner-block">Neil Patton Practitioner Group</div>
  </section>

</main>
</body>
</html>
```